Website for software company "velmor"

We need a website for our software company/startup named "velmor". We are developing several products (currently 3 standard-software products) which are all in different sectors, but all our products are available for Laptops/PC/Mobile Phones/Tablets, ... We do also create custom software and support our customers with consulting to optimize their processes.
We already have a Logo which you can find in the attached files.
We are a young team of 4 members (two founders and 2 employees).

To get an idea of our products -> the first one is a planning software for healthcare organizations (eg. HelpWing, firebrigade, pharmacy), the second one is a booking software for sport clubs and the third one is a competition software for sports hunting. You see very diverse. Include or ignore this info of our products as you like.

The design has to be a bootstrap 4 (or higher) design. We have licenced FontAwesome as iconset. Responsive design should come without saying.

• Starting page, product pages, news section, contact, team, services

```html
<!DOCTYPE html>
<html lang="en">
<head>
<meta charset="utf-8">
<title>velmor — Build. Grow. Innovate.</title>
<link href="https://fonts.googleapis.com/css2?family=Rubik:wght@400;500;600&family=Montserrat:wght@400;500;600;700;800&display=swap" rel="stylesheet">
<style>
:root{
  --navy:#232a35;
  --navy-deep:#1b2029;
  --orange:#f5812b;
  --ink:#2a2f38;
  --body:#4d525b;
  --muted:#9aa0a8;
  --rule:#c9ccd1;
  --paper:#ffffff;
  --mist:#f3f3f4;
  --field:#ebebed;
}
*{box-sizing:border-box;margin:0;padding:0}
html,body{width:1200px;height:4539px;overflow:hidden}
body{position:relative;background:var(--paper);font-family:"Montserrat",sans-serif;color:var(--body)}
.abs{position:absolute}
.heading{font-family:"Rubik",sans-serif;font-weight:500;color:var(--ink);letter-spacing:.2px}
.tri{display:inline-block;width:0;height:0;border-top:7px solid transparent;border-bottom:7px solid transparent;border-left:10px solid var(--orange);vertical-align:middle}
.copy{font-size:13.5px;line-height:25px;color:var(--body)}
.learn{font-family:"Montserrat",sans-serif;font-size:15px;letter-spacing:2.5px;color:var(--orange);text-decoration:underline;text-underline-offset:4px}
.learn .tri{margin-right:12px;border-top-width:7px;border-bottom-width:7px;border-left-width:11px}
.btn{display:flex;align-items:center;border:2px solid var(--orange);height:50px;width:183px;font-family:"Rubik",sans-serif;font-weight:500;font-size:14px}
.btn .btn-icon{width:52px;height:100%;background:var(--orange);display:flex;align-items:center;justify-content:center;margin-right:12px}
.photo{box-shadow:0 14px 30px rgba(0,0,0,.14)}

/* hero */
.hero-panel{left:0;top:0;width:645px;height:703px;background:var(--navy)}
.brand{font-family:"Rubik",sans-serif;font-weight:500;font-size:46px;letter-spacing:1px;color:#fff;display:flex;align-items:center;gap:12px}
.brand-mark{width:14px;height:14px;background:var(--orange)}
.hero-title{left:108px;top:210px;font-family:"Montserrat",sans-serif;font-weight:800;font-size:54px;line-height:68px;color:#fff}
.hero-title .dot{color:var(--orange);font-size:30px}
.hero-lede{left:110px;top:356px;width:320px;font-size:14px;line-height:22px;color:#fff}
.menu{left:1002px;top:58px;display:flex;align-items:center;gap:10px;font-family:"Rubik",sans-serif;font-weight:500;font-size:13px;color:var(--ink)}
.menu-dot{width:38px;height:38px;border-radius:50%;background:var(--navy);display:flex;flex-direction:column;justify-content:center;align-items:center;gap:4px}
.menu-dot i{display:block;width:16px;height:2px;background:#fff}
.scroll-label{left:491px;top:517px;transform:rotate(-90deg);transform-origin:center;width:110px;font-family:"Rubik",sans-serif;font-size:13px;color:#fff;letter-spacing:.5px;text-align:center}
.follow{left:690px;top:675px;display:flex;align-items:center;gap:6px;font-family:"Rubik",sans-serif;font-size:13px;color:var(--ink)}
.social-dot{width:24px;height:24px;border-radius:50%;background:var(--navy)}
.follow .line{width:75px;height:1px;background:var(--orange);margin:0 12px 0 14px}

/* about */
.who-box{left:110px;top:789px;width:409px;height:113px;background:var(--orange);display:flex;align-items:center;padding-left:42px}
.who-box span{font-size:16px;letter-spacing:3.5px;color:var(--ink);font-weight:500}
.who-box i{display:block;width:165px;height:3px;background:var(--navy);margin-left:32px}
.section-h{font-size:28px}
.product-h{font-size:24px}

/* why */
.why-panel{left:600px;top:2254px;width:600px;height:587px;background:var(--navy)}
.why-copy{left:712px;top:2428px;width:370px;font-size:13.5px;line-height:24.5px;color:#e9eaec}

/* news */
.card{width:310px;height:330px;background:#fff;box-shadow:0 6px 20px rgba(0,0,0,.12)}
.card .pic{height:180px}
.card h3{font-family:"Rubik",sans-serif;font-weight:500;font-size:18px;color:var(--ink);margin:20px 10px 8px}
.card p{font-size:12px;line-height:20px;color:var(--body);margin:0 10px}
.card .learn{display:block;font-size:12px;letter-spacing:2px;margin:14px 10px 0}
.card .learn .tri{border-top-width:6px;border-bottom-width:6px;border-left-width:9px;margin-right:10px}

/* contact */
.contact-band{left:0;top:3465px;width:1200px;height:680px;background:var(--mist)}
.field-label{font-size:14px;color:var(--ink)}
.field-label b{color:var(--orange);font-weight:400}
.field-line{height:1px;background:#b9bcc2;width:514px}
.captcha{left:350px;top:4005px;width:218px;height:53px;background:#fafafa;border:1px solid #dcdcdc;display:flex;align-items:center;padding-left:16px;gap:10px;font-size:9px;color:var(--ink)}
.captcha .box{width:16px;height:16px;border:1.5px solid #c1c1c1;background:#fff}
.captcha .badge{margin-left:auto;margin-right:26px;width:26px;height:26px;border-radius:4px;background:#c9d3e3}

/* footer */
.footer{left:0;top:4145px;width:1200px;height:340px;background:var(--navy)}
.footer-bar{left:0;top:4485px;width:1200px;height:54px;background:var(--navy-deep)}
.foot-h{font-family:"Rubik",sans-serif;font-weight:500;font-size:18px;color:#fff}
.foot-text{font-size:11px;line-height:19.5px;color:#8c929b}
.foot-links{font-size:12px;line-height:26px;color:#8c929b;list-style:none}
.foot-item{display:flex;align-items:flex-start;gap:12px;font-size:12px;line-height:24px;color:#8c929b}
.foot-icon{width:18px;height:18px;border-radius:50%;background:#3b424e;flex:none;display:flex;align-items:center;justify-content:center;margin-top:3px}
.subscribe{left:830px;top:4355px;width:247px;height:42px;border-radius:21px;background:#fff;overflow:hidden;display:flex;align-items:center}
.subscribe span{font-size:11px;color:#8c929b;padding-left:14px;display:flex;align-items:center;gap:6px;flex:1}
.subscribe .send{width:54px;height:100%;background:var(--orange);display:flex;align-items:center;justify-content:center}
.foot-social{left:840px;top:4417px;display:flex;gap:9px}
.foot-social i{display:block;width:26px;height:26px;border-radius:50%;background:#fff}
.foot-social i.hot{background:var(--orange)}
.legal{font-size:12px;color:#fff}
</style>
</head>
<body>

<!-- HERO -->
<div class="abs hero-panel"></div>
<div class="abs brand" style="left:110px;top:36px"><span class="brand-mark"></span>VELMOR</div>
<div class="abs menu">MENU <span class="menu-dot"><i></i><i></i><i></i></span></div>

<h1 class="abs hero-title">BUILD<span class="dot">.</span>GROW<span class="dot">.</span><br>INNOVATE<span class="dot">.</span></h1>
<p class="abs hero-lede">Lorem ipsum dolor sitamet consectetur adipiscing elitsed doeiusmod</p>
<a class="abs btn" style="left:110px;top:432px;color:#fff">
  <span class="btn-icon"><svg width="20" height="12" viewBox="0 0 20 12"><path d="M1 6h17M13 1l5 5-5 5" stroke="#fff" stroke-width="1.6" fill="none"/></svg></span>JOIN THE TEAM
</a>
<div class="abs scroll-label">SCROLL DOWN</div>
<svg class="abs" style="left:537px;top:585px" width="16" height="96" viewBox="0 0 16 96"><line x1="8" y1="0" x2="8" y2="82" stroke="var(--orange)" stroke-width="1.5"/><path d="M2 82h12L8 93z" fill="var(--orange)"/></svg>

<div class="abs photo" role="img" aria-label="Young developer smiling at his laptop" style="left:611px;top:154px;width:124px;height:425px;background:linear-gradient(180deg,#cfc8bf,#9a8a7e)"></div>
<div class="abs photo" role="img" aria-label="Two colleagues discussing work at a desk" style="left:805px;top:154px;width:372px;height:432px;background:linear-gradient(180deg,#c9c3bb,#6f6a6c)"></div>

<div class="abs follow"><span class="social-dot"></span><span class="social-dot"></span><span class="social-dot"></span><span class="line"></span>FOLLOW US</div>

<!-- ABOUT -->
<div class="abs who-box"><span>WHO WE ARE</span><i></i></div>
<h2 class="abs heading section-h" style="left:110px;top:914px"><span class="tri" style="margin-right:12px"></span>ABOUT <span style="color:var(--orange)">VELMOR</span></h2>
<p class="abs copy" style="left:133px;top:954px;width:430px">Lorem ipsum dolor sitamet consectetur adipiscing elitsedo eiusmod tempor incididuntut laboreet dolore magna aliquat enim adminim veniamquis nostrud exercitation.</p>

<div class="abs photo" role="img" aria-label="Medical staff walking along a hospital corridor" style="left:640px;top:867px;width:406px;height:388px;background:linear-gradient(135deg,#6f7f8e,#d8dde2 55%,#8a9aa8)"></div>
<h2 class="abs heading product-h" style="left:660px;top:1296px">HEALTHCARE ORGANIZATIONS</h2>
<p class="abs copy" style="left:662px;top:1340px;width:430px">Lorem ipsum dolor sitamet consectetur adipiscing elitsedo eiusmod tempor incididuntut laboreet dolore magna aliquat enim adminim veniamquis nostrud exercitation.</p>
<a class="abs learn" style="left:640px;top:1440px"><span class="tri"></span>LEARN MORE</a>

<div class="abs photo" role="img" aria-label="Footballer juggling a ball on a sunlit pitch" style="left:112px;top:1232px;width:405px;height:387px;background:linear-gradient(160deg,#e6b56a,#8c8a3e 45%,#3f5a24)"></div>
<h2 class="abs heading product-h" style="left:132px;top:1660px">SPORT CLUBS</h2>
<p class="abs copy" style="left:133px;top:1704px;width:430px">Lorem ipsum dolor sitamet consectetur adipiscing elitsedo eiusmod tempor incididuntut laboreet dolore magna aliquat enim adminim veniamquis nostrud exercitation.</p>
<a class="abs learn" style="left:110px;top:1804px"><span class="tri"></span>LEARN MORE</a>

<div class="abs photo" role="img" aria-label="Runners racing along a forest trail" style="left:640px;top:1576px;width:406px;height:388px;background:linear-gradient(160deg,#c89a5c,#5d6a34 45%,#8b8360)"></div>
<h2 class="abs heading product-h" style="left:660px;top:2004px">SPORTS HUNTING</h2>
<p class="abs copy" style="left:662px;top:2048px;width:430px">Lorem ipsum dolor sitamet consectetur adipiscing elitsedo eiusmod tempor incididuntut laboreet dolore magna aliquat enim adminim veniamquis nostrud exercitation.</p>
<a class="abs learn" style="left:640px;top:2148px"><span class="tri"></span>LEARN MORE</a>

<!-- WHY CHOOSE US -->
<div class="abs why-panel"></div>
<div class="abs photo" role="img" aria-label="Team gathered around a laptop in a bright office" style="left:110px;top:2323px;width:568px;height:447px;background:linear-gradient(150deg,#b7b9b8,#e8e8e6 50%,#8f9496)"></div>
<h2 class="abs heading section-h" style="left:688px;top:2375px;color:#fff"><span class="tri" style="margin-right:12px"></span>WHY CHOOSE US</h2>
<p class="abs why-copy">Lorem ipsum dolor sitamet consectetur adipiscing elitsedo eiusmod tempor incididuntut laboreet dolore magna aliquat enim adminim veniamquis nostrud exercitation dolor sitamet consectetur adipiscing elitsedo eiusmod tempor incididuntut laboreet dolore magna aliquat enim adminim veniamquis nostrud exercitation dolor sitamet consectetur adipiscing elitsedo eiusmod tempo.</p>
<a class="abs btn" style="left:712px;top:2664px;color:#fff">
  <span class="btn-icon"><svg width="20" height="12" viewBox="0 0 20 12"><path d="M1 6h17M13 1l5 5-5 5" stroke="#fff" stroke-width="1.6" fill="none"/></svg></span>LEARN MORE
</a>

<!-- NEWS -->
<h2 class="abs heading section-h" style="left:0;width:1200px;text-align:center;top:2976px"><span class="tri" style="margin-right:12px"></span>OUR LATEST NEWS AND UPDATES</h2>

<article class="abs card" style="left:110px;top:3040px">
  <div class="pic" role="img" aria-label="Colleagues celebrating in a meeting room" style="background:linear-gradient(150deg,#5f6469,#c9c5bf 55%,#3e4248)"></div>
  <h3>Consectetur adipiscingelit</h3>
  <p>Lorem ipsum dolor sitamet consectetur adip iscing elitsedo eiusmod tempor incidid untut laboreet dolore.</p>
  <a class="learn"><span class="tri"></span>LEARN MORE</a>
</article>
<article class="abs card" style="left:445px;top:3040px">
  <div class="pic" role="img" aria-label="Team high-fiving over a work table" style="background:linear-gradient(150deg,#d9d3cb,#9a6f63 50%,#cfc7bd)"></div>
  <h3>Consectetur adipiscingelit</h3>
  <p>Lorem ipsum dolor sitamet consectetur adip iscing elitsedo eiusmod tempor incidid untut laboreet dolore.</p>
  <a class="learn"><span class="tri"></span>LEARN MORE</a>
</article>
<article class="abs card" style="left:780px;top:3040px">
  <div class="pic" role="img" aria-label="Colleagues working together at a laptop by a window" style="background:linear-gradient(150deg,#9fb3c4,#e3e4e5 50%,#4a4c52)"></div>
  <h3>Consectetur adipiscingelit</h3>
  <p>Lorem ipsum dolor sitamet consectetur adip iscing elitsedo eiusmod tempor incidid untut laboreet dolore.</p>
  <a class="learn"><span class="tri"></span>LEARN MORE</a>
</article>

<!-- CONTACT -->
<div class="abs contact-band"></div>
<h2 class="abs heading section-h" style="left:0;width:1200px;text-align:center;top:3540px"><span class="tri" style="margin-right:12px"></span>CONTACT US</h2>
<p class="abs" style="left:0;width:1200px;text-align:center;top:3588px;font-size:14px;color:var(--ink)">Lorem ipsum dolorsitamet consectetur adipiscing elitsed doeiusmod</p>

<label class="abs field-label" style="left:348px;top:3641px">Name <b>*</b></label>
<div class="abs field-line" style="left:348px;top:3671px"></div>
<label class="abs field-label" style="left:348px;top:3696px">Phone <b>*</b></label>
<div class="abs field-line" style="left:348px;top:3726px"></div>
<label class="abs field-label" style="left:348px;top:3751px">Email <b>*</b></label>
<div class="abs field-line" style="left:348px;top:3781px"></div>
<label class="abs field-label" style="left:348px;top:3806px">Message</label>
<div class="abs" style="left:348px;top:3838px;width:514px;height:152px;background:var(--field)"></div>

<div class="abs captcha"><span class="box"></span>I'm not a robot<span class="badge"></span></div>
<a class="abs btn" style="left:703px;top:4010px;width:157px;color:var(--ink)">
  <span class="btn-icon" style="width:46px"><svg width="20" height="12" viewBox="0 0 20 12"><path d="M1 6h17M13 1l5 5-5 5" stroke="#fff" stroke-width="1.6" fill="none"/></svg></span>SUBMIT
</a>

<!-- FOOTER -->
<footer>
<div class="abs footer"></div>
<div class="abs brand" style="left:110px;top:4222px"><span class="brand-mark"></span>VELMOR</div>
<p class="abs foot-text" style="left:110px;top:4290px;width:225px">Lorem ipsum dolor sitamet consectetur adipiscing elitsedo eiusmod tempor incididuntut laboreet dolore magna aliquat enim adminim veniamquis nostrud exercitation dolor sitamet consectetur adipiscing elitsed.</p>

<h3 class="abs foot-h" style="left:397px;top:4225px">QUICK LINKS</h3>
<span class="abs tri" style="left:398px;top:4256px;border-top-width:6px;border-bottom-width:6px;border-left-width:9px"></span>
<ul class="abs foot-links" style="left:397px;top:4280px"><li>Home</li><li>About Us</li><li>What We Do</li><li>Blog</li><li>Contact</li></ul>

<h3 class="abs foot-h" style="left:585px;top:4225px">CONTACT US</h3>
<span class="abs tri" style="left:586px;top:4256px;border-top-width:6px;border-bottom-width:6px;border-left-width:9px"></span>
<div class="abs foot-item" style="left:583px;top:4284px"><span class="foot-icon"><svg width="10" height="10" viewBox="0 0 10 10"><path d="M2 1l2 2-1 1.5c.7 1.3 1.5 2.1 2.5 2.5L7 6l2 2-1.5 1.5C4.5 9 1 5.5.5 2.5z" fill="#c9ccd1"/></svg></span>+43 100 200 3040</div>
<div class="abs foot-item" style="left:583px;top:4318px"><span class="foot-icon"><svg width="10" height="8" viewBox="0 0 10 8"><rect x=".5" y=".5" width="9" height="7" fill="none" stroke="#c9ccd1"/><path d="M.5 .5l4.5 4 4.5-4" fill="none" stroke="#c9ccd1"/></svg></span>info.velmor@mail.com</div>
<div class="abs foot-item" style="left:583px;top:4352px"><span class="foot-icon"><svg width="8" height="11" viewBox="0 0 8 11"><path d="M4 0a4 4 0 0 1 4 4c0 3-4 7-4 7S0 7 0 4a4 4 0 0 1 4-4z" fill="#c9ccd1"/><circle cx="4" cy="4" r="1.4" fill="#3b424e"/></svg></span>Lindenweg 12, Altbrunn<br>Austria, 4410.</div>

<h3 class="abs foot-h" style="left:840px;top:4225px">SUBSCRIBE TO OUR BLOG</h3>
<span class="abs tri" style="left:841px;top:4256px;border-top-width:6px;border-bottom-width:6px;border-left-width:9px"></span>
<p class="abs foot-text" style="left:838px;top:4286px;width:260px;line-height:21px">Sign up today to get resources on how to attract and retain more customers!</p>
<div class="abs subscribe"><span><svg width="11" height="8" viewBox="0 0 11 8"><rect width="11" height="8" rx="1" fill="var(--orange)"/><path d="M.5 .5l5 4 5-4" fill="none" stroke="#fff"/></svg>Email Address</span><span class="send"><svg width="20" height="20" viewBox="0 0 20 20"><path d="M2 9l16-7-6 16-2.5-6.5z" fill="none" stroke="#fff" stroke-width="1.6" stroke-linejoin="round"/></svg></span></div>
<div class="abs foot-social"><i></i><i class="hot"></i><i></i></div>
</footer>

<div class="abs footer-bar"></div>
<p class="abs legal" style="left:110px;top:4505px">Copyright © 2022 <span style="color:var(--orange);text-decoration:underline">Velmor</span> . All rights reserved.</p>
<p class="abs legal" style="left:803px;top:4505px">Terms and Conditions</p>
<p class="abs legal" style="left:970px;top:4505px">I</p>
<p class="abs legal" style="left:1000px;top:4505px">Privacy Policy</p>

</body>
</html>
```